Stationery Design Project

I am a personal trainer in the fitness industry based in Miami. I have recently designed a logo for my company, now i need to market my name through selected stationery designs.
I need an email signature, invoice and a business card. I am looking for a design that is fresh and eye catching to my target audience.
Updates

Reason: Waiting for photo to be taken for business card.

Target Market(s)

25 to 65 years old - male and female - overweight, sedentary and athletic clientele - middle to wealthy economic class

Industry/Entity Type

Personal Trainer

Requirements
Must have
• Will attach Zip file with logo, template of invoice and personal information.
Will attach photo for business card in the next few days.
Nice to have
• Black backdrop logo image for banner of Invoice, with transparent images of my logo.
White backdrop logo image for Email signature, with font that works well with logo.

```html
<!DOCTYPE html>
<html lang="en">
<head>
<meta charset="utf-8">
<title>Kinetic Pulse Studio – Business Card</title>
<link rel="stylesheet" href="https://fonts.googleapis.com/css2?family=Montserrat:wght@500;700&family=Allura&display=swap">
<style>
  :root {
    --card-bg: #000000;
    --brand-silver: #e4e4e4;
    --contact-white: #ffffff;
    --flame-red: #e8261a;
    --flame-orange: #f57c10;
    --flame-yellow: #fcd21c;
    --mark-amber: #f6a500;
  }
  html, body {
    margin: 0;
    padding: 0;
    width: 1200px;
    height: 686px;
    overflow: hidden;
    background: var(--card-bg);
  }
  .business-card {
    position: relative;
    width: 1200px;
    height: 686px;
    background: var(--card-bg);
    overflow: hidden;
  }
  .brand-name {
    position: absolute;
    top: 22px;
    left: 0;
    width: 1200px;
    margin: 0;
    text-align: center;
    font-family: "Montserrat", sans-serif;
    font-weight: 700;
    color: var(--brand-silver);
    line-height: 1;
    text-transform: uppercase;
  }
  .brand-name .brand-line-main {
    display: block;
    font-size: 78px;
    letter-spacing: 2px;
  }
  .brand-name .brand-line-sub {
    display: block;
    margin-top: 18px;
    font-size: 46px;
    letter-spacing: 9px;
  }
  .brand-mark {
    position: absolute;
    left: 748px;
    top: 200px;
    width: 390px;
    height: 390px;
  }
  .trainer-name {
    position: absolute;
    left: 44px;
    top: 262px;
    margin: 0;
    font-family: "Allura", cursive;
    font-weight: 400;
    font-size: 100px;
    line-height: 1.1;
    background: linear-gradient(90deg, var(--flame-red) 0%, var(--flame-orange) 40%, var(--flame-yellow) 100%);
    -webkit-background-clip: text;
    background-clip: text;
    color: transparent;
  }
  .contact-list {
    position: absolute;
    left: 48px;
    top: 400px;
    margin: 0;
    padding: 0;
    list-style: none;
    font-family: "Montserrat", sans-serif;
    font-weight: 500;
    font-size: 31px;
    font-variant: small-caps;
    letter-spacing: 3.5px;
    color: var(--contact-white);
  }
  .contact-list li {
    height: 51.5px;
    line-height: 51.5px;
    white-space: nowrap;
  }
</style>
</head>
<body>
  <main class="business-card">
    <h1 class="brand-name">
      <span class="brand-line-main">Kinetic Pulse</span>
      <span class="brand-line-sub">Studio</span>
    </h1>

    <svg class="brand-mark" viewBox="0 0 390 390" aria-hidden="true">
      <circle cx="195" cy="195" r="185" fill="var(--mark-amber)"/>
    </svg>

    <h2 class="trainer-name">Dana Marlow</h2>

    <ul class="contact-list">
      <li class="contact-role">Personal Fitness Trainer</li>
      <li class="contact-cell">(C) 555-214-7730</li>
      <li class="contact-work">(W) 555-386-0192</li>
      <li class="contact-web">Kineticpulsestudio.com</li>
      <li class="contact-email">dana@kineticpulsestudio.com</li>
    </ul>
  </main>
</body>
</html>
```